New flavour! New packaging for Velocity Energy Drink!

We need a new packaging designed to show off our new grape flavored energy drink! It will require box design with matching sachets!

Established in 2018 we are a fully Australian owned and operated business that started out with 2 gamers that got sick and tired of sugary energy drinks OR expensive powder from the USA.

We are an energy drink in the esports and gaming space. Our new product is an energy drink in powder in boxes of 30 sachets (please see attached for product example)

Please see example 1 and 2 for our competitors product. We would ideally like to go a bit more minimalist than them but still have a great color pop on black backing.

Target Market(s)

Gamer's and esports athletes between the ages or 18-30

Font styles to use
Sans Serif
Other font styles liked:
• Helvetica

Colors
886aae
ffffff

Requirements
Must have
• Black base/background.
• Vibrant purple N in the Velocity Logo.
• Same or slightly different shades of purple for some text and highlights.
• Black, white and some shades of a vibrant purple (for the grape flavor)
• ingredients list (may need to be reformatted to suit)
• Please see attached for legislative requirements on the box and sachets.
Nice to have
• minimalist design but enough to be eye catching and somewhat playful
• Twitter: @VLCT_FUEL
• Instagram: @VLCT_FUEL
• Facebook: @VLCTFUEL
Should not have
• OTHER COLORS.
• Overly complex designs.

```html
<!DOCTYPE html>
<html lang="en">
<head>
<meta charset="utf-8">
<title>Velocity Energy Drink – Grape Flavour Carton</title>
<link href="https://fonts.googleapis.com/css2?family=Russo+One&family=Arimo:wght@400;700&display=swap" rel="stylesheet">
<style>
  :root{
    --page:#ffffff;
    --panel:#19191b;
    --panel-line:#232326;
    --flap:#2f2f32;
    --purple:#886aae;
    --purple-vivid:#7b48c0;
    --white:#ffffff;
    --ink:#111111;
    --grape-a:#a04a6e;
    --grape-b:#6e2a48;
  }
  html,body{margin:0;padding:0;width:723px;height:1200px;overflow:hidden;background:var(--page);}
  .canvas{position:relative;width:723px;height:1200px;}
  .dieline{position:absolute;left:0;top:352px;width:904px;height:620px;transform:scale(.8);transform-origin:0 0;font-family:"Arimo",Helvetica,sans-serif;color:var(--white);}
  .dieline svg.cut{position:absolute;left:0;top:0;}
  .panel{position:absolute;top:130px;height:350px;overflow:hidden;}
  .back{left:48px;width:285px;}
  .side-left{left:333px;width:107px;}
  .front{left:440px;width:275px;}
  .side-right{left:715px;width:110px;}

  /* back panel */
  .info{position:absolute;left:43px;top:36px;width:90px;font-size:6.2px;line-height:1.35;}
  .info h4{margin:0 0 4px;font-size:7px;font-weight:700;}
  .info p{margin:0 0 8px;}
  .nutrition{position:absolute;left:142px;top:38px;width:128px;height:222px;background:var(--white);color:var(--ink);padding:5px 6px;box-sizing:border-box;font-size:4.6px;}
  .nutrition h3{margin:0 0 2px;font-size:10px;font-weight:700;}
  .nutrition .serve{border-top:2px solid var(--ink);padding-top:2px;line-height:1.4;font-weight:700;}
  .nutrition table{width:100%;border-collapse:collapse;margin-top:3px;}
  .nutrition th,.nutrition td{border-top:.6px solid #777;padding:2.4px 1px;text-align:right;font-weight:700;}
  .nutrition th:first-child,.nutrition td:first-child{text-align:left;}
  .nutrition td.sub{padding-left:14px;}
  .nutrition tr.band td{border-top:1.4px solid var(--ink);}
  .best{position:absolute;left:207px;top:265px;font-size:7px;font-weight:700;}
  .origin{position:absolute;left:202px;top:320px;font-size:7px;font-weight:700;}

  /* front */
  .brand{position:absolute;left:0;right:0;top:70px;text-align:center;font-family:"Russo One",sans-serif;font-size:34px;letter-spacing:1px;color:var(--white);}
  .flavour{position:absolute;left:0;right:0;top:160px;text-align:center;font-family:"Russo One",sans-serif;font-size:14.5px;color:var(--purple-vivid);}
  .claim{position:absolute;left:0;right:0;top:180px;text-align:center;font-family:"Russo One",sans-serif;font-size:10.5px;line-height:1.45;}
  .grapes{position:absolute;left:90px;top:245px;width:100px;height:100px;border-radius:48% 52% 45% 55%;background:radial-gradient(circle at 40% 40%,var(--grape-a),var(--grape-b));}
  .weight{position:absolute;left:38px;top:287px;width:58px;height:22px;border:1.4px solid var(--white);text-align:center;font-family:"Russo One",sans-serif;font-size:8px;line-height:10px;padding-top:1px;box-sizing:border-box;}
  .serves{position:absolute;left:185px;top:287px;width:58px;text-align:center;font-family:"Russo One",sans-serif;font-size:8px;line-height:12px;}
  .serves span{display:block;border-top:1.4px solid var(--white);margin-top:1px;}

  /* sides */
  .vertical{position:absolute;top:0;left:0;width:350px;height:107px;transform-origin:0 0;transform:translateX(107px) rotate(90deg);}
  .vertical .brand-v{position:absolute;left:52px;top:8px;font-family:"Russo One",sans-serif;font-size:32px;letter-spacing:1px;}
  .vertical .lines{position:absolute;left:52px;top:55px;font-family:"Russo One",sans-serif;font-size:9.5px;line-height:1.3;}
</style>
</head>
<body>
<div class="canvas">
  <div class="dieline">
    <svg class="cut" width="904" height="620" viewBox="0 0 904 620" aria-hidden="true">
      <defs>
        <pattern id="lines" width="14" height="14" patternUnits="userSpaceOnUse" patternTransform="rotate(35)">
          <rect width="14" height="14" fill="#19191b"/>
          <line x1="0" y1="0" x2="0" y2="14" stroke="#232326" stroke-width="1"/>
        </pattern>
      </defs>
      <!-- top flaps -->
      <path d="M345 130 L352 70 L440 70 L440 130 Z" fill="#2f2f32"/>
      <path d="M440 130 L440 70 L460 70 L460 22 Q460 10 472 10 L700 10 Q712 10 712 22 L712 70 L715 70 L715 130 Z" fill="#2f2f32"/>
      <path d="M715 130 L715 70 L805 70 L825 130 Z" fill="#2f2f32"/>
      <!-- bottom flaps -->
      <path d="M48 480 L330 480 L330 595 L70 595 Q48 595 48 575 Z" fill="#2f2f32"/>
      <path d="M333 480 L440 480 L440 555 L345 555 Z" fill="#2f2f32"/>
      <path d="M440 480 L715 480 L715 555 L440 555 Z" fill="#2f2f32"/>
      <path d="M715 480 L825 480 L815 555 L715 555 Z" fill="#2f2f32"/>
      <!-- glue flap -->
      <path d="M825 130 L868 145 L868 465 L825 480 Z" fill="#2f2f32"/>
      <!-- main panels -->
      <rect x="48" y="130" width="777" height="350" fill="url(#lines)"/>
      <line x1="333" y1="130" x2="333" y2="480" stroke="#3a3a3d" stroke-width=".8"/>
      <line x1="440" y1="130" x2="440" y2="480" stroke="#3a3a3d" stroke-width=".8"/>
      <line x1="715" y1="130" x2="715" y2="480" stroke="#3a3a3d" stroke-width=".8"/>
    </svg>

    <section class="panel back">
      <div class="info">
        <h4>INGREDIENT LISTING:</h4>
        <p>Acidity regulator (citric acid, sodium citrate), mineral salt (sodium bicarbonate), taurine, natural grape juice powder (8.5%) (maltodextrin, sugar, grape juice concentrate), caffeine (2.8%), inositol, vitamins (B3, B1, B6, B2), ginseng extract (0.5%), sweetener (steviol glycoside), mineral salt (magnesium stearate).</p>
        <p>Store in a cool dry place, away from sunlight below 25o C.</p>
        <p>Keep away from children</p>
        <h4>DIRECTIONS FOR USE:</h4>
        <p>Place one sachet in 400 ml water, stir until dissolved, and consume immediately.</p>
        <h4>USAGE: <span style="font-weight:400">Maximum of two sachets per day</span></h4>
        <p></p>
        <h4>IMPORTED BY:</h4>
        <p>Pixel Fuel Trading Pty Ltd<br>42 Harbour Lane<br>Geelong VIC 3220<br>Australia<br>www.velocityfuel.shop</p>
      </div>
      <div class="nutrition">
        <h3>Nutrition Facts</h3>
        <div class="serve">SERVINGS PER PACKAGE: (30)<br>SERVING SIZE: 5g powder &amp; 400 ml water</div>
        <table>
          <tr><th></th><th>AV. QTY PER<br>SERVING</th><th>AV. QTY<br>PER 100 ml</th></tr>
          <tr class="band"><td>ENERGY</td><td>5 kJ</td><td>1 kJ</td></tr>
          <tr><td>PROTEIN</td><td>0.0 g</td><td>0.0 g</td></tr>
          <tr><td>FAT TOTAL</td><td>0.0 g</td><td>0.0 g</td></tr>
          <tr><td class="sub">Saturated Fat</td><td>0.0 g</td><td>0.0 g</td></tr>
          <tr><td>CARBOHYDRATE</td><td>0.3 g</td><td>0.1 g</td></tr>
          <tr><td class="sub">Sugars</td><td>0.0 g</td><td>0.0 g</td></tr>
          <tr><td>SODIUM</td><td>250 mg</td><td>62 mg</td></tr>
          <tr class="band"><td colspan="3">COMPOSITION INFORMATION</td></tr>
          <tr><td>Caffeine</td><td>100 mg</td><td>25 mg</td></tr>
          <tr><td>Thiamin (B1)</td><td>10 mg</td><td>2.5 mg</td></tr>
          <tr><td>Riboflavin (B2)</td><td>5 mg</td><td>1.2 mg</td></tr>
          <tr><td>Niacin (B3)</td><td>20 mg</td><td>5 mg</td></tr>
          <tr><td>B6 (Pyridoxine)</td><td>5 mg</td><td>1.2 mg</td></tr>
          <tr><td>Taurine</td><td>500 mg</td><td>125 mg</td></tr>
          <tr><td>Inositol</td><td>50 mg</td><td>12.5 mg</td></tr>
        </table>
      </div>
      <div class="best">Best Before:</div>
      <div class="origin">Made in China</div>
    </section>

    <section class="panel side-left">
      <div class="vertical">
        <div class="brand-v">VELOCITY</div>
        <div class="lines">Grape flavour<br>With Ginseng &amp; Caffeine For<br>gamers,By gamers</div>
      </div>
    </section>

    <section class="panel front">
      <div class="brand">VELOCITY</div>
      <div class="flavour">GRAPE FLAVOUR</div>
      <div class="claim">With Ginseng &amp; Caffeine For<br>gamers,By gamers</div>
      <div class="grapes" role="img" aria-label="Photo of a bunch of red grapes with vine leaves"></div>
      <div class="weight">150g<br>(30x5g)</div>
      <div class="serves">30<span>Serves</span></div>
    </section>

    <section class="panel side-right">
      <div class="vertical">
        <div class="brand-v">VELOCITY</div>
        <div class="lines">Grape flavour<br>With Ginseng &amp; Caffeine For<br>gamers,By gamers</div>
      </div>
    </section>
  </div>
</div>
</body>
</html>
```